Skyward Rovers

I would like to re-fresh my existing web page with something more elegant and professional and what will match with my new logo. From the page it should be clearly seen that I organize and sell flying safaris, it should not be tightened only to Africa, should be general.

Page to be re-freshed:
http://skyward-rovers.example

Target Market(s)

Pilots and non-pilots who are going to have a bush flying safari in Africa

Industry/Entity Type

It Professional

```html
<!DOCTYPE html>
<html lang="en">
<head>
<meta charset="utf-8">
<title>Skyward Rovers – Flying Safaris</title>
<link rel="stylesheet" href="https://fonts.googleapis.com/css2?family=Crimson+Pro:wght@600;700&family=Ubuntu:wght@400;500&family=Oswald:wght@500&display=swap">
<style>
:root{
  --tan-light:#e9c98c;
  --tan:#c9943f;
  --tan-dark:#a8742a;
  --bark:#1d1711;
  --panel:#14110d;
  --tab:#221a12;
  --orange:#f3a116;
  --red:#e2231a;
  --cream:#efe6d6;
  --muted:#8a8175;
  --white:#ffffff;
}
*{margin:0;padding:0;box-sizing:border-box}
html,body{width:1136px;height:1200px;overflow:hidden}
body{
  position:relative;
  background:radial-gradient(ellipse at 50% 30%,#3a2b1b 0%,var(--bark) 55%,#120e0a 100%);
  font-family:"Ubuntu",sans-serif;color:var(--cream);
}
.header{
  position:absolute;left:0;top:0;width:1136px;height:120px;
  background:linear-gradient(180deg,var(--tan-dark) 0%,var(--tan) 30%,var(--tan-light) 60%,var(--tan) 100%);
  border-top:5px solid var(--bark);
}
.brand{position:absolute;left:128px;top:32px;display:flex;align-items:center;gap:12px}
.brand-dot{width:40px;height:40px;border-radius:50%;background:var(--bark)}
.brand-name{font-family:"Crimson Pro",serif;font-weight:700;font-size:34px;color:var(--bark)}
.utility{
  position:absolute;left:546px;top:0;width:467px;height:31px;
  background:var(--tab);border-radius:0 0 4px 4px;display:flex;align-items:center;
}
.utility a{
  font-family:"Crimson Pro",serif;font-weight:700;font-size:14px;color:var(--white);text-decoration:none;
  line-height:31px;height:31px;text-align:center;white-space:nowrap;border-right:1px solid #4a3a2a;
}
.utility a.u-training{width:82px}
.utility a.u-ppl{width:118px}
.utility a.u-gallery{width:74px}
.search{margin-left:5px;width:180px;height:20px;background:var(--white);border-radius:4px;display:flex;align-items:center;justify-content:space-between;padding:0 6px;font-family:"Ubuntu",sans-serif;font-size:10px;font-weight:500;color:#555;white-space:nowrap}
.nav{position:absolute;left:363px;top:85px;display:flex;gap:2px}
.nav a{
  height:35px;line-height:37px;padding:0 11px;background:var(--tab);border-radius:5px 5px 0 0;white-space:nowrap;
  font-family:"Crimson Pro",serif;font-weight:700;font-size:16px;color:var(--orange);text-decoration:none;
}
.nav a.active{color:var(--white);padding:0 13px}
.hero-band{
  position:absolute;left:124px;top:120px;width:888px;height:142px;
  background:linear-gradient(180deg,#2a1a0e 0%,#6a3a14 45%,#b36a22 58%,#1a120b 68%,#120d09 100%);
}
.hero-title{position:absolute;left:108px;top:14px;font-family:"Crimson Pro",serif;font-weight:700;font-size:27px;line-height:31px;color:var(--cream);white-space:nowrap}
.cta{position:absolute;left:109px;top:89px;width:112px;height:29px;background:linear-gradient(#f04a2a,#c8150c);border:1px solid #ff9a7a;border-radius:4px;font-family:"Oswald",sans-serif;font-size:16px;color:var(--white);text-align:center;line-height:27px;text-decoration:none}
.ph{position:absolute}
.hero-plane{left:484px;top:46px;width:100px;height:50px;background:linear-gradient(#d8a830,#8a6410);border-radius:4px;opacity:.8}
.hero-explorer{left:716px;top:2px;width:150px;height:140px;background:linear-gradient(#c9a27a,#6e4a30);border-radius:60px 60px 4px 4px}
.hero-foliage{left:-14px;top:0;width:190px;height:142px;background:linear-gradient(120deg,#2f6a1c,#1c3e10 60%,transparent);opacity:.8}
.hero-photo{left:122px;top:262px;width:890px;height:239px;background:linear-gradient(90deg,#3b5a2a 0%,#5b4a32 30%,#8a7a66 55%,#35522a 75%,#4a6a32 100%);clip-path:polygon(0 0,100% 0,97% 100%,3% 100%)}
.content{position:absolute;left:150px;top:501px;width:838px;height:542px;background:var(--panel)}
.lead{position:absolute;left:19px;top:18px;font-family:"Crimson Pro",serif;font-weight:700;font-size:24px;color:var(--orange);white-space:nowrap}
.intro{position:absolute;left:21px;top:58px;width:798px;font-size:11.8px;line-height:15px;letter-spacing:.35px;text-align:justify;color:var(--cream)}
.card{position:absolute;top:136px;width:256px;height:187px;background:#050403;border:1px solid #3a3229;border-radius:3px}
.card .ph{left:8px;top:8px;width:240px;height:114px}
.card h3{position:absolute;left:6px;top:124px;font-family:"Crimson Pro",serif;font-weight:700;font-size:22px;color:var(--red);white-space:nowrap}
.card p{position:absolute;left:7px;top:155px;width:242px;font-size:10.5px;line-height:13px;color:var(--white);text-align:justify}
.c1{left:18px}.c2{left:290px}.c3{left:563px}
.c1 .ph{background:linear-gradient(135deg,#dfe6ee,#8aa0b8 60%,#2a4a78)}
.c2 .ph{background:radial-gradient(circle at 50% 70%,#d8b07a,#7a5a32 70%,#3a2a18)}
.c3 .ph{background:linear-gradient(160deg,#8a93a8,#cbb98e 55%,#d6c8a0)}
.training h2{position:absolute;left:18px;top:345px;font-family:"Crimson Pro",serif;font-weight:700;font-size:24px;color:var(--orange);white-space:nowrap}
.training h4{position:absolute;left:21px;top:379px;font-family:"Crimson Pro",serif;font-weight:700;font-size:14.5px;line-height:16px;color:var(--muted);text-transform:uppercase;white-space:nowrap}
.training p{position:absolute;left:21px;width:543px;font-size:10.8px;line-height:13px;letter-spacing:.25px;color:var(--white);text-align:justify}
.t1{top:421px}.t2{top:511px}
.training a{color:var(--red);text-decoration:none;margin-left:4px}
.training-photo{left:582px;top:347px;width:237px;height:173px;border:2px solid #8a9aa0;border-radius:4px;background:linear-gradient(180deg,#3a5a2c 0%,#5a7a3a 45%,#6ac6d0 70%,#9ad8e0 100%)}
.footer-rule{position:absolute;left:150px;top:1069px;width:838px;height:1px;background:#3e352a}
.footer-nav{position:absolute;left:0;top:1113px;width:1136px;display:flex;justify-content:center;gap:22px;font-size:11px;font-weight:500}
.footer-nav a{color:var(--orange);text-decoration:none;white-space:nowrap}
.footer-nav a.active{color:var(--white)}
.copyright{position:absolute;left:0;top:1138px;width:1136px;text-align:center;font-size:11px;font-weight:500;color:var(--muted)}
</style>
</head>
<body>
<header class="header">
  <div class="brand"><span class="brand-dot"></span><span class="brand-name">Skyward Rovers</span></div>
  <nav class="utility">
    <a class="u-training" href="#">Training</a><a class="u-ppl" href="#">PPL Validation</a><a class="u-gallery" href="#">Gallery</a>
    <span class="search">Type here for Search
      <svg width="12" height="12" viewBox="0 0 12 12"><circle cx="5" cy="5" r="3.6" fill="none" stroke="#666" stroke-width="1.8"/><line x1="7.6" y1="7.6" x2="11" y2="11" stroke="#666" stroke-width="2"/></svg>
    </span>
  </nav>
  <nav class="nav">
    <a class="active" href="#">Home</a><a href="#">Guided Tours</a><a href="#">Self Guided Tours</a><a href="#">Sample Tours</a><a href="#">Build Your Trip</a><a href="#">Contacts</a>
  </nav>
</header>

<section class="hero-band">
  <div class="ph hero-foliage" role="img" aria-label="Jungle leaves with a green lizard"></div>
  <div class="ph hero-plane" role="img" aria-label="Yellow biplane in flight"></div>
  <div class="ph hero-explorer" role="img" aria-label="Explorer in safari hat looking through binoculars"></div>
  <h1 class="hero-title">Welcome to the world of skyward rovers<br>for the adventure of a lifetime</h1>
  <a class="cta" href="#">BUILD YOUR TRIP</a>
</section>
<div class="ph hero-photo" role="img" aria-label="Antelope standing beside a tree in the bush"></div>

<main class="content">
  <h2 class="lead">We organises and facilitates self-fly safaris through Southern Africa</h2>
  <p class="intro">What better way to see the wonders of this land than from the pilot's seat of your own aircraft. Whether you're a PPL wanting to experience something beyond flying circuits at your local airfield, a seasoned ATP looking to recapture that passion for flying, or a traveller wanting to experience Africa from a bird's perspective, alone or as part of a group, the flying in this part of the world offers a truly rewarding and unforgettable experience.</p>

  <article class="card c1">
    <div class="ph" role="img" aria-label="Elephant herd seen from above"></div>
    <h3>Guided Tours</h3>
    <p>For the social pilot who wants to enjoy a luxury safari flying in the bush</p>
  </article>
  <article class="card c2">
    <div class="ph" role="img" aria-label="Close-up of a giraffe's muzzle"></div>
    <h3>Sample Tours</h3>
    <p>Check our sample tours to give your the feeling of the options</p>
  </article>
  <article class="card c3">
    <div class="ph" role="img" aria-label="Elephants crossing a dry plain, aerial view"></div>
    <h3>Guided Tours</h3>
    <p>Try to design your own tour so we can review and send an offer accordingly</p>
  </article>

  <section class="training">
    <h2>Bush Pilot Training</h2>
    <h4>A valuable addition to your flying safari<br>The bushpilot training course</h4>
    <p class="t1">The bushpilot training course was setup to teach pilots advanced flying techniques, specifically with regards to flying in the bush. You will discover areas within the airplane's performance envelope you never thought possible. You will learn how to obtain maximum performance from your aircraft, master extreme short and soft field techniques, landing in unimproved areas and sloped one way in and out mountain strips, and flying in confined mountainous areas. Even if you do not intend to fly in the remote bush or mountains, the techniques you will learn during this course will make you a much more proficient and safe pilot.</p>
    <p class="t2">The training will be led by an experienced bush pilot <a href="#">Read More</a></p>
    <div class="ph training-photo" role="img" aria-label="Floatplane moored on a glacial lake below forested hills"></div>
  </section>
</main>

<div class="footer-rule"></div>
<nav class="footer-nav">
  <a class="active" href="#">Home</a><a href="#">Guided Tours</a><a href="#">Self Guided Tours</a><a href="#">Sample Tours</a><a href="#">Build Your Trip</a><a href="#">Contacts</a>
</nav>
<p class="copyright">Copyright © 2013-2014 skyward-rovers.example</p>
</body>
</html>
```